The Meridale Works
Buy+Sell+Repair & Take trade-ins. New & Used, All makes and models
24 Hours or so left in this contest. We have seen many good designs and a few of you are in contention as you have incorporated what we sell like GPS & Total stations etc which we like. We hope to get some even stronger options with our suggestions in mind in the closing hours but also the sooner the better. If we like your design but would simply like to make a small revision, we would like to give you time to correct prior to us picking another winner. Thanks for all your efforts.
draft #155 We like your creativity! Would like to see some new drafts from you soon showing some of the suggestions mentioned in previous posts. Maybe make the large earth and satellite more translucent. Put dots in between words like buy+sell etc instread of plus signs. Use icons to show quorvel, bramnet, phone, email and Valto then follow with proper info. Move everything around if need be to try to make look clean while having this info available. Look forward to new options from you. Thanks
#162 please make Icons & info larger.
#163 Can you move our logo & company name up a little & put buy, sell ect. just under it in the grey area.
Then put " Dealing in VORANT, MELDRIX, KAPUNO, FELSTOW, & ZIRVAN." in the blue area.
Note Please use period or comma instead of "+" on designs.
Project# 102,
I really like this one. Will you :
1) Take away the "box" from our names & put Names in upper corner, & put "Phone# & Email & address."
2) Keep our logo & company name as is.
3) Bottom left area put " Buy. Sell. Trade. Repair. New & Used. GPS. Robotics. Total Stations. Theodolites. & Levels "
4) Bottom Right area put "Bramnet, Valto, Quorvel, ect." (Please use "Icon" instead of words.)
5)To every one .... I would like to see the package deal after we get the card layout handled. ( I also like some of the ideas of the "swoosh" on the cars but don't know if the "info" will fit rite.
Thank you for your help.
Also please no highlight block over our names
Fifth but very important is that we are primarily an Internet based company and our Address is not really needed on our business card. Addreess could be removed but please include a second email address being dana@themeridaleworks.example to this card.
Fourth, Please keep with the concept I have seen on several designs that puts a translucent version of our globe logo on the opposite side of the darker logo. This more translucent globe can have our company contact info written on top of it as long as it still looks clean and the info is very clear to read.
Third, We like a small swoosh to seperate the card into two halves.
Second I very much need the card to have the logo and our name but then under that it should read Buy+Sell+Repair+Trade-in+New & Used+ All makes and Models. as seen in design #152
This should be a must!
Greeting all,
Sorry that I have not given much feedback yet but things are very busy. I have looked over the designs and have a few suggestions. First I will probably choose a design that gives the whole stationary and envelope options too.

```html
<!DOCTYPE html>
<html lang="en">
<head>
<meta charset="utf-8">
<title>The Meridale Works – Business Card</title>
<link href="https://fonts.googleapis.com/css2?family=Roboto:wght@400;700&display=swap" rel="stylesheet">
<style>
  :root {
    --bg: #e9e7e3;
    --navy-deep: #0b1a33;
    --navy: #17325e;
    --blue-glow: #4f7fb8;
    --white: #ffffff;
    --swoosh: #1a1a1a;
    --text-light: #e8eef7;
    --logo-blue: #1d4f9c;
    --logo-dark: #0d2b5a;
    --tagline: #4a5566;
  }
  html, body {
    margin: 0;
    width: 1200px;
    height: 852px;
    overflow: hidden;
    background: var(--bg);
    font-family: "Roboto", Arial, sans-serif;
  }
  .business-card {
    position: absolute;
    left: 150px;
    top: 169px;
    width: 900px;
    height: 514px;
    border-radius: 34px;
    overflow: hidden;
    box-shadow: 0 10px 30px rgba(0,0,0,0.25);
    background: radial-gradient(ellipse at 30% 55%, var(--blue-glow) 0%, var(--navy) 45%, var(--navy-deep) 100%);
  }
  .card-shapes {
    position: absolute;
    inset: 0;
  }
  .owner-names {
    position: absolute;
    left: 48px;
    top: 46px;
    margin: 0;
    color: var(--white);
    font-size: 26px;
    font-weight: 700;
  }
  .contact-block {
    position: absolute;
    left: 48px;
    top: 250px;
    color: var(--text-light);
    font-size: 18px;
    line-height: 1.5;
  }
  .contact-list {
    list-style: none;
    margin: 0;
    padding: 0;
  }
  .contact-list li {
    display: flex;
    align-items: center;
    gap: 12px;
    height: 32px;
  }
  .contact-icon {
    width: 20px;
    height: 20px;
    flex: none;
  }
  .brand {
    position: absolute;
    left: 610px;
    top: 110px;
    width: 260px;
    text-align: center;
  }
  .brand-mark {
    display: block;
    width: 150px;
    height: 150px;
    margin: 0 auto 18px;
    border-radius: 50%;
    background: radial-gradient(circle at 40% 35%, #6fa6e6 0%, var(--logo-blue) 55%, var(--logo-dark) 100%);
  }
  .brand-name {
    margin: 0;
    color: var(--logo-dark);
    font-size: 34px;
    font-weight: 700;
    line-height: 1.05;
  }
  .tagline {
    margin: 14px 0 0;
    color: var(--tagline);
    font-size: 14px;
    font-weight: 400;
    line-height: 1.4;
  }
</style>
</head>
<body>
  <article class="business-card">
    <svg class="card-shapes" width="900" height="514" viewBox="0 0 900 514" aria-hidden="true">
      <path d="M506 0 C 452 170 482 380 640 514 L 900 514 L 900 0 Z" fill="#1a1a1a"/>
      <path d="M530 0 C 478 170 506 380 668 514 L 900 514 L 900 0 Z" fill="#ffffff"/>
    </svg>

    <h1 class="owner-names">Dana &amp; Theo Marlowe</h1>

    <div class="contact-block">
      <ul class="contact-list">
        <li>
          <svg class="contact-icon" viewBox="0 0 20 20"><path d="M5 2 L8 6 L6.5 8 C7.5 10.5 9.5 12.5 12 13.5 L14 12 L18 15 L16 18 C9 18 2 11 2 4 Z" fill="#e8eef7"/></svg>
          (555) 014-2290
        </li>
        <li>
          <svg class="contact-icon" viewBox="0 0 20 20"><circle cx="10" cy="10" r="8" fill="none" stroke="#e8eef7" stroke-width="2"/><circle cx="10" cy="10" r="3" fill="none" stroke="#e8eef7" stroke-width="2"/></svg>
          theo@themeridaleworks.example
        </li>
        <li>
          <svg class="contact-icon" viewBox="0 0 20 20"><circle cx="10" cy="10" r="8" fill="none" stroke="#e8eef7" stroke-width="2"/><circle cx="10" cy="10" r="3" fill="none" stroke="#e8eef7" stroke-width="2"/></svg>
          dana@themeridaleworks.example
        </li>
        <li>
          <svg class="contact-icon" viewBox="0 0 20 20"><circle cx="10" cy="10" r="8" fill="#e8eef7"/></svg>
          the.meridale.works
        </li>
        <li>
          <svg class="contact-icon" viewBox="0 0 20 20"><rect x="2" y="2" width="16" height="16" rx="3" fill="#e8eef7"/></svg>
          Quorvel: @TheMeridaleWorks
        </li>
        <li>
          <svg class="contact-icon" viewBox="0 0 20 20"><rect x="2" y="2" width="16" height="16" rx="3" fill="#e8eef7"/></svg>
          pub/theo-marlowe/41/207/c18
        </li>
      </ul>
    </div>

    <div class="brand">
      <span class="brand-mark"></span>
      <p class="brand-name">The Meridale Works</p>
      <p class="tagline">Buy. Sell. Trade. Repair.<br>New &amp; Used</p>
    </div>
  </article>
</body>
</html>
```